Riverbend Trusted Home Care-Flyer for Patients

Our Home Health Care Agency, Riverbend Trusted Home Care, is seeking a flyer to advertise our services. We would like our flyer to convey professionalism, classiness and sophistication. We want our agency to come across as one that is well-established and recognized as being first-rate within the field.

We also want to appear original; we want to stand out.

Our theme colors, blue and green, from our logo should be incorporated into the flyer's design (refer below).

The top of the page should say (in a clear, bold font)-Seeking Care for your Loved One?

Our Logo, followed by our slogan, "Lean On Those Nearby", should be in the center. (This should make it appear as if our agency is the obvious solution to the consumer's quest in finding suitable care for their family member). This should be in a big font.
Below that, our agency's services should be listed in a very noticeable font...yet smaller than what's written above that.
The text should read:
Our Services Include:
*Experienced Certified Home Health Aides/ Live In Home Health Aides/Companions
*Nursing Services
*Alzheimer’s and Dementia Care
*Respite Care
*Postoperative Care
*Post Rehabilitation Care
*Running Errands
*Light Housekeeping
*Assistance with Bathing, Feeding and Grooming
*Meal Preparation
*Laundry and Linen Washing
*Mail and Bill Organization
*Medication Management
*Accompanying to Doctor’s Appointments
*And much more!
Below that, in a smaller, yet noticeable font:
As seasoned professionals, we know how to help our clients navigate and fulfill their various health care needs. Those nearby are here to help you get the attention that you merit.
Call Riverbend Trusted Home Care today to learn more about our first-rate services!
Below that, in a larger font, our phone number, website, our e-mail address.
*Out contact information will be provided to the project’s winner*.

*Pictures of Caregivers helping elderly patient should be included in the advertisement as well. *

We provided advertisements of other Home Health Care Agencies attached below to use as a reference. Once again, while we are aiming for a similar idea; however, our goal is to stand out as the community's premiere home health care agency, the one that they want to choose. We want to be original as well!

Size: Standard Computer Paper Size. 8.5” x 11”.

Feel free to utilize your creative, designer flair!
We look forward to seeing the results!
Good luck!

Industry/Entity Type

Home Health Care

Font styles to use
Sans Serif

Requirements
Must have
• Refer above.
Nice to have
• Refer to attachment below to see how other home health care agencies advertise. While we are aiming for a similar idea, we would like to incorporate our logo, slogan and colors to make this flyer more unique and stand out. We would like to appear original.

```html
<!DOCTYPE html>
<html lang="en">
<head>
<meta charset="utf-8">
<title>Riverbend Trusted Home Care – Flyer</title>
<link rel="stylesheet" href="https://fonts.googleapis.com/css2?family=Barlow+Condensed:wght@500;600;700;800&family=Open+Sans:wght@400;600&display=swap">
<style>
:root{
  --green:#4e9a2a;
  --green-bright:#6cc24a;
  --navy:#14245a;
  --blue:#26418f;
  --blue-deep:#1a2f6e;
  --white:#ffffff;
  --page:#555555;
}
*{margin:0;padding:0;box-sizing:border-box}
html,body{width:1200px;height:2400px;overflow:hidden;background:var(--page)}
.flyer{position:absolute;left:0;top:423px;width:1200px;height:1553px;overflow:hidden;background:linear-gradient(180deg,#fafafa,#f1f1ef);font-family:"Open Sans",sans-serif;color:var(--white)}
.photo-main{position:absolute;left:660px;top:0;width:540px;height:900px;background:linear-gradient(160deg,#f4f4f2 0%,#dfe4ea 30%,#3c6fc7 52%,#2f5cb5 70%,#ece9e4 100%)}
.photo-circle{position:absolute;left:-40px;top:400px;width:470px;height:470px;border-radius:50%;border:8px solid var(--green-bright);background:linear-gradient(135deg,#efeae2 0%,#d9cdbb 45%,#f2efe9 70%,#c9b49a 100%);z-index:3}
.headline{position:absolute;left:58px;top:48px;z-index:4}
.headline .lead{font-family:"Barlow Condensed",sans-serif;font-weight:800;font-size:124px;line-height:1;color:var(--green);letter-spacing:1px}
.headline .follow{font-family:"Barlow Condensed",sans-serif;font-weight:800;font-size:88px;line-height:1;color:var(--navy)}
.headline .intro{font-family:"Barlow Condensed",sans-serif;font-weight:600;font-size:37px;line-height:45px;color:#111;margin-top:12px;width:640px}
.wave{position:absolute;left:0;top:0;width:1200px;height:1553px;z-index:2}
.brand-disc{position:absolute;left:428px;top:508px;width:345px;height:345px;border-radius:50%;background:var(--white);border:9px solid var(--green-bright);z-index:5;display:flex;flex-direction:column;align-items:center;justify-content:center;text-align:center}
.brand-disc .dot{width:66px;height:66px;border-radius:50%;background:var(--blue);margin-bottom:14px}
.brand-disc .name{font-family:"Barlow Condensed",sans-serif;font-weight:700;font-size:32px;line-height:34px;color:var(--blue);text-transform:uppercase;width:290px}
.brand-disc .slogan{font-family:"Barlow Condensed",sans-serif;font-weight:700;font-size:18px;letter-spacing:2px;color:var(--green);text-transform:uppercase;margin-top:8px}
.statement{position:absolute;left:0;width:1200px;top:905px;text-align:center;font-family:"Barlow Condensed",sans-serif;font-weight:700;font-size:36px;line-height:46px;text-transform:uppercase;z-index:4}
.services{position:absolute;left:62px;top:1031px;width:1073px;height:264px;border:3px solid var(--green-bright);border-radius:20px;z-index:4}
.services .tab{position:absolute;left:298px;top:-27px;width:470px;height:56px;border-radius:28px;background:var(--green);font-family:"Barlow Condensed",sans-serif;font-weight:700;font-size:36px;line-height:56px;text-align:center}
.services .col{position:absolute;top:50px;list-style:none;font-size:19px;line-height:22px}
.services .col li{position:relative;padding-left:24px;margin-bottom:11px}
.services .col li::before{content:"";position:absolute;left:0;top:6px;width:9px;height:9px;border-radius:50%;background:var(--green-bright)}
.col-one{left:52px}.col-two{left:432px}.col-three{left:784px}
.services .divider{position:absolute;top:52px;height:175px;border-left:2px dotted var(--green-bright)}
.about{position:absolute;left:0;width:1200px;top:1312px;text-align:center;font-size:21px;line-height:28px;z-index:4}
.cta-rule{position:absolute;left:66px;top:1419px;width:1069px;height:3px;background:var(--green-bright);z-index:4}
.cta{position:absolute;left:115px;top:1393px;width:970px;height:56px;border-radius:28px;background:var(--green);font-family:"Barlow Condensed",sans-serif;font-weight:700;font-size:24px;line-height:56px;text-align:center;text-transform:uppercase;white-space:nowrap;z-index:5}
.contacts{position:absolute;left:0;width:1200px;top:1472px;display:flex;justify-content:center;gap:44px;font-size:25px;line-height:34px;z-index:5}
.contacts span{display:flex;align-items:center;gap:10px}
.contacts svg{width:20px;height:20px;fill:var(--green-bright)}
</style>
</head>
<body>
<main class="flyer">
  <div class="photo-main" role="img" aria-label="Photo of a smiling nurse in blue scrubs helping an elderly woman in a white robe"></div>

  <svg class="wave" viewBox="0 0 1200 1553" aria-hidden="true">
    <path d="M0,858 C220,830 430,835 600,865 C800,900 1020,880 1200,810 L1200,1553 L0,1553 Z" fill="var(--blue)"/>
    <path d="M640,866 C830,905 1030,880 1200,790 L1200,812 C1020,892 820,910 640,872 Z" fill="var(--green-bright)"/>
    <path d="M0,1460 L0,1553 L260,1553 Z" fill="var(--blue-deep)"/>
    <path d="M1200,1450 L1200,1553 L930,1553 Z" fill="var(--blue-deep)"/>
  </svg>

  <header class="headline">
    <h1 class="lead">SEEKING CARE</h1>
    <h2 class="follow">FOR YOUR LOVED ONE?</h2>
    <p class="intro">This should make it appear as if our agency is the obvious solution to the consumer's quest in finding suitable care for their family member</p>
  </header>

  <div class="photo-circle" role="img" aria-label="Photo of a caregiver in white helping a smiling elderly woman with a cane"></div>

  <div class="brand-disc">
    <div class="dot"></div>
    <div class="name">Riverbend Trusted Home Care</div>
    <div class="slogan">Lean On Those Nearby</div>
  </div>

  <p class="statement">This should make it appear as if our agency is the obvious solution to<br>the consumer's quest in finding suitable care for their family member</p>

  <section class="services">
    <div class="tab">OUR SERVICES INCLUDE:</div>
    <ul class="col col-one">
      <li>Alzheimer’s and Dementia Care</li>
      <li>Laundry and Linen Washing</li>
      <li>Mail and Bill Organization</li>
      <li>And much more!</li>
      <li>Accompanying to<br>Doctor’s Appointments</li>
    </ul>
    <div class="divider" style="left:385px"></div>
    <ul class="col col-two">
      <li>Nursing Services</li>
      <li>Light Housekeeping</li>
      <li>Meal Preparation</li>
      <li>Respite Care</li>
      <li>Experienced Certified Home<br>Health Aides/ Live In Home<br>Health Aides/Companions</li>
    </ul>
    <div class="divider" style="left:735px"></div>
    <ul class="col col-three">
      <li>Postoperative Care</li>
      <li>Post Rehabilitation Care</li>
      <li>Medication Management</li>
      <li>Running Errands</li>
      <li>Assistance with Bathing,<br>Feeding and Grooming</li>
    </ul>
  </section>

  <p class="about">As seasoned professionals, we know how to help our clients navigate and fulfill their various<br>health care needs. Those nearby are here to help you get the attention that you merit.</p>

  <div class="cta-rule"></div>
  <p class="cta">Call Riverbend Trusted Home Care today to learn more about our first-rate services!</p>

  <footer class="contacts">
    <span><svg viewBox="0 0 24 24"><path d="M6.6 10.8a15.1 15.1 0 0 0 6.6 6.6l2.2-2.2a1 1 0 0 1 1-.25 11.4 11.4 0 0 0 3.6.57 1 1 0 0 1 1 1V20a1 1 0 0 1-1 1A17 17 0 0 1 3 4a1 1 0 0 1 1-1h3.5a1 1 0 0 1 1 1c0 1.25.2 2.45.57 3.57a1 1 0 0 1-.25 1z"/></svg>1(555)-014-2087</span>
    <span><svg viewBox="0 0 24 24"><path d="M2 5h20v14H2z M2 5l10 8 10-8" fill="none" stroke="var(--green-bright)" stroke-width="2.4"/></svg>info@riverbendtrusted.com</span>
    <span><svg viewBox="0 0 24 24"><circle cx="12" cy="12" r="9" fill="none" stroke="var(--green-bright)" stroke-width="2.4"/><path d="M3 12h18M12 3c3 3 3 15 0 18M12 3c-3 3-3 15 0 18" fill="none" stroke="var(--green-bright)" stroke-width="1.8"/></svg>riverbendtrusted.com</span>
  </footer>
</main>
</body>
</html>
```